Yoga Training Cerificate

Design a certificate of graduation from a Vinyasa Yoga Teacher Training Program.

The attached document is an example of the certificate I received as a graduate from a teacher training program. You can use it as a template.

Stylistically, what you design can be: visually enticing, professional, clean, and modern.

Please develop the "Lumen Stretch" logo and embed it within the certificate.

Please add a circular watermark behind the body of the certificate similar to the one found in the attachment; leave out the words Asana Guildhall because I am not associated with that organization.

The name of my school is "Lumen Stretch." And it was established in 2017, which you can include.

The certificate affirms that "' 'such-and-such' has successfully completed the Lumen Stretch modern vinyasa yoga training, completing two hundred hours of instruction in practice and theory. Within the power of our institution as a certifying agent we declare Such-and-such, now, a teacher competent to share the gift of yoga with the masses in a safe and effective."

My name -Dennis Whitcombe- should be at bottom with a faux-signature; position title: Lumen Stretch founder.

If you decide to include text on the fringe, like the example, it might include bars of text describing the maxims of the Lumen Stretch school reading:

This is Lumen Stretch
Breath is primary
Evolve the physical culture
Bring your unique expression to the practice
Take Breaks
Freestyle
Close your eyes
Feel deeper into your body
This is active meditation
This is moving meditation
This is modern meditation

And find a way to integrate Emojis like: Fire, Water, Prayer Hands, etc. as you see fit.

Generally, make the certificate look: official, clear and clean. You can base it from the example given. And try and create a graphic design that is more visually capturing then the example.

```html
<!DOCTYPE html>
<html lang="en">
<head>
<meta charset="utf-8">
<title>Lumen Stretch – Certificate of Completion</title>
<link rel="stylesheet" href="https://fonts.googleapis.com/css2?family=Great+Vibes&family=Raleway:wght@300;400&family=Roboto:wght@300;400&family=Roboto+Condensed:wght@400;700&display=swap">
<style>
  :root {
    --paper: #ffffff;
    --ink: #1e1e1e;
    --ink-soft: #6b6b6b;
    --rule: #2a2a2a;
    --divider: #555555;
    --seal: #d9d9d9;
    --brand: #6e6e6e;
  }
  * { margin: 0; padding: 0; box-sizing: border-box; }
  html, body { width: 1200px; height: 849px; overflow: hidden; background: var(--paper); }
  .certificate { position: relative; width: 1200px; height: 849px; background: var(--paper); color: var(--ink); }

  .maxims { position: absolute; left: 78px; top: 122px; list-style: none;
    font-family: "Raleway", sans-serif; font-weight: 300; font-size: 16px; color: var(--ink-soft); }
  .maxims li { height: 46.5px; line-height: 24px; }

  .brand { position: absolute; left: 94px; top: 646px; display: flex; align-items: center; gap: 16px;
    font-family: "Raleway", sans-serif; font-weight: 300; font-size: 44px; color: var(--brand); }
  .brand-dot { width: 46px; height: 46px; border-radius: 50%; background: var(--brand); }

  .divider { position: absolute; left: 481px; top: 108px; width: 2px; height: 632px; background: var(--divider); }

  .seal { position: absolute; left: 598px; top: 146px; width: 480px; height: 480px; }

  .content { position: absolute; left: 500px; width: 680px; text-align: center; }
  .title { top: 146px; font-family: "Great Vibes", cursive; font-size: 72px; line-height: 90px; letter-spacing: -0.5px; }
  .affirms { top: 234px; font-family: "Roboto", sans-serif; font-weight: 300; font-size: 18px; }
  .name-rule { position: absolute; left: 605px; top: 336px; width: 465px; height: 3px; background: var(--rule); }
  .body { font-family: "Roboto", sans-serif; font-weight: 300; font-size: 22.5px; line-height: 28.5px; }
  .body-completed { top: 359px; }
  .body-declare { top: 483px; }
  .blank { display: inline-block; width: 204px; border-bottom: 3px solid var(--rule); vertical-align: -2px; }

  .sign-rule { position: absolute; height: 3px; background: var(--rule); }
  .sign-founder { left: 518px; top: 666px; width: 264px; }
  .sign-date { left: 986px; top: 666px; width: 140px; }
  .signer { position: absolute; text-align: center; font-family: "Roboto Condensed", sans-serif; }
  .signer-name { left: 500px; width: 300px; top: 674px; font-weight: 700; font-size: 25px; }
  .signer-role { left: 500px; width: 300px; top: 705px; font-family: "Roboto", sans-serif; font-weight: 300; font-size: 21px; }
  .date-label { left: 986px; width: 140px; top: 674px; font-weight: 700; font-size: 25px; }
</style>
</head>
<body>
<main class="certificate">
  <ul class="maxims">
    <li>This is Lumen Stretch</li>
    <li>Breath is primary</li>
    <li>Evolve the physical culture</li>
    <li>Bring your unique expression to the practice</li>
    <li>Take Breaks</li>
    <li>Freestyle</li>
    <li>Close your eyes</li>
    <li>Feel deeper into your body</li>
    <li>This is active meditation</li>
    <li>This is moving meditation</li>
    <li>This is modern meditation</li>
  </ul>

  <div class="brand"><span class="brand-dot"></span><span class="brand-name">Lumen Stretch</span></div>

  <div class="divider"></div>

  <svg class="seal" viewBox="0 0 480 480" aria-hidden="true">
    <circle cx="240" cy="240" r="226" fill="none" stroke="var(--seal)" stroke-width="24"/>
  </svg>

  <h1 class="content title">Certificate of Completion</h1>
  <p class="content affirms">The certificate affirms that</p>
  <div class="name-rule"></div>

  <p class="content body body-completed">has successfully completed<br>
    The Lumen Stretch modern vinyasa yoga training<br>
    completing two hundred hours of<br>
    instruction in practice and theory.</p>

  <p class="content body body-declare">Within the power of our institution as a certifying agent<br>
    we declare <span class="blank"></span>, now, a teacher<br>
    competent to share the gift of yoga<br>
    with the masses in a safe and effective manner.</p>

  <div class="sign-rule sign-founder"></div>
  <p class="signer signer-name">DENNIS WHITCOMBE</p>
  <p class="signer signer-role">LUMEN STRETCH FOUNDER</p>

  <div class="sign-rule sign-date"></div>
  <p class="signer date-label">DATE</p>
</main>
</body>
</html>
```